Autora necesita un cover para su nuevo libro acerca de empoderamiento femenino*

Diseño de cover para libro digital sobre empoderamiento femenino.

El título del libro es: "Las 7 Raíces del Alma Luminosa"
Subtítulo: Se una mujer valiente, serena y plena

Autora: Rosaura Beltrán

Target Market(s)

Mujeres

Font styles to use
Sans Serif

Requirements
Must have
• El título del libro es: "Las 7 Raíces del Alma Luminosa"

Autora: Rosaura Beltrán
Should not have
• Sin imágenes

```html
<!DOCTYPE html>
<html lang="es">
<head>
<meta charset="UTF-8">
<title>Las 7 Raíces del Alma Luminosa — Rosaura Beltrán</title>
<link rel="stylesheet" href="https://fonts.googleapis.com/css2?family=Oswald:wght@500;600&family=Kaushan+Script&family=Caveat:wght@500&display=swap">
<style>
  :root {
    --page-bg: #ffffff;
    --cover-black: #0a0006;
    --cover-plum: #4a0440;
    --cover-magenta: #b3089a;
    --gold: #e9b43c;
    --gold-light: #f6d27a;
    --gold-deep: #c4861f;
    --ink-white: #ffffff;
  }
  * { margin: 0; padding: 0; box-sizing: border-box; }
  html, body {
    width: 1200px;
    height: 800px;
    overflow: hidden;
    background: var(--page-bg);
  }
  .stage {
    width: 1200px;
    height: 800px;
    display: flex;
    align-items: center;
    justify-content: center;
  }
  .book-cover {
    position: relative;
    width: 530px;
    height: 760px;
    background: radial-gradient(ellipse 62% 50% at 50% 56%,
      var(--cover-magenta) 0%, #8e0679 38%, var(--cover-plum) 68%, var(--cover-black) 100%);
    overflow: hidden;
  }
  .title {
    position: absolute;
    top: 44px;
    left: 0;
    width: 100%;
    padding: 0 30px;
    text-align: center;
  }
  .title-line {
    display: block;
    font-family: "Oswald", sans-serif;
    font-weight: 500;
    color: var(--gold);
    text-transform: uppercase;
    line-height: 1;
    letter-spacing: -1px;
    font-size: 90px;
    transform: scaleY(1.1);
  }
  .title-line--second { margin-top: 6px; }
  .title-article {
    font-family: "Kaushan Script", cursive;
    font-size: 56px;
    color: var(--ink-white);
    text-transform: none;
    letter-spacing: 0;
    margin-right: 8px;
    display: inline-block;
    transform: rotate(-6deg) scaleY(0.9);
    vertical-align: 8px;
  }
  .title-script {
    display: block;
    font-family: "Kaushan Script", cursive;
    font-size: 84px;
    line-height: 1;
    color: var(--ink-white);
    margin-top: 8px;
    transform: rotate(-3deg);
  }
  .pillars-art {
    position: absolute;
    top: 382px;
    left: 60px;
    width: 410px;
    height: 190px;
    border-radius: 4px;
    background: linear-gradient(90deg, var(--gold-deep), var(--gold-light) 30%, var(--gold) 55%, var(--gold-light) 78%, var(--gold-deep));
    opacity: 0.92;
  }
  .subtitle {
    position: absolute;
    top: 592px;
    left: 0;
    width: 100%;
    text-align: center;
    font-family: "Caveat", cursive;
    font-weight: 500;
    font-size: 33px;
    line-height: 1.05;
    color: var(--ink-white);
    transform: rotate(-4deg);
  }
  .author {
    position: absolute;
    bottom: 30px;
    left: 0;
    width: 100%;
    text-align: center;
    font-family: "Oswald", sans-serif;
    font-weight: 600;
    font-size: 30px;
    line-height: 1.2;
    letter-spacing: 7px;
    color: var(--gold);
    text-transform: uppercase;
  }
</style>
</head>
<body>
  <main class="stage">
    <article class="book-cover">
      <h1 class="title">
        <span class="title-line"><span class="title-article">Las</span>7 Raíces</span>
        <span class="title-line title-line--second">del Alma</span>
        <span class="title-script">Luminosa</span>
      </h1>
      <div class="pillars-art" role="img" aria-label="Ilustración de una hilera de columnas clásicas doradas"></div>
      <p class="subtitle">Se una mujer valiente,<br>serena y plena</p>
      <p class="author">Rosaura Beltrán</p>
    </article>
  </main>
</body>
</html>
```